Brulo Dumpsters Flikto Banner

Need a Flikto banner made with my buisness information and logo and company colors. Company information and colors and design can be tasken from uploaded photos.

```html
<!DOCTYPE html>
<html lang="en">
<head>
<meta charset="utf-8">
<title>Brulo Dumpsters – Flikto Banner</title>
<link rel="stylesheet" href="https://fonts.googleapis.com/css2?family=Michroma&family=Montserrat:wght@500&display=swap">
<style>
  :root {
    --canvas-grey: #414143;
    --sky: #29a8e0;
    --bright-blue: #00aeef;
    --deep-blue: #0e63ae;
    --pill-blue: #2a5db5;
    --sun: #f9cb16;
    --leaf: #8cc462;
    --white: #ffffff;
  }
  * { box-sizing: border-box; margin: 0; padding: 0; }
  html, body { width: 1200px; height: 675px; overflow: hidden; }
  body {
    position: relative;
    background: var(--canvas-grey);
    font-family: "Michroma", sans-serif;
    color: var(--white);
  }
  .size-label {
    position: absolute;
    right: 10px;
    top: 215px;
    font-family: "Montserrat", sans-serif;
    font-weight: 500;
    font-size: 11.5px;
    letter-spacing: 0.4px;
  }
  .banner {
    position: absolute;
    left: 0;
    top: 240px;
    width: 1200px;
    height: 199px;
    overflow: hidden;
    background: var(--sky);
  }
  .banner-art { position: absolute; inset: 0; width: 1200px; height: 199px; }
  .recycle-mark {
    position: absolute;
    left: 160px;
    top: 19px;
    width: 50px;
    height: 46px;
    border-radius: 50%;
    background: rgba(255, 255, 255, 0.18);
  }
  .brand-lockup {
    position: absolute;
    left: 334px;
    top: 32px;
    display: flex;
    align-items: center;
    gap: 26px;
  }
  .brand-dot {
    width: 92px;
    height: 92px;
    border-radius: 50%;
    background: var(--sun);
  }
  .brand-name {
    font-size: 44px;
    font-weight: 400;
    line-height: 1;
    letter-spacing: 1px;
    white-space: nowrap;
    color: var(--white);
  }
  .service-line {
    position: absolute;
    left: 508px;
    width: 284px;
    top: 131px;
    text-align: center;
    font-size: 12.5px;
    letter-spacing: 3px;
    white-space: nowrap;
    color: var(--white);
  }
  .web-pill {
    position: absolute;
    left: 542px;
    top: 161px;
    width: 216px;
    height: 26px;
    border-radius: 13px;
    border: 1px solid rgba(255, 255, 255, 0.7);
    background: linear-gradient(180deg, #3a78d0 0%, var(--pill-blue) 100%);
    display: flex;
    align-items: center;
    justify-content: center;
    overflow: hidden;
    white-space: nowrap;
    font-size: 7.6px;
    letter-spacing: 0.5px;
    color: var(--white);
  }
</style>
</head>
<body>
  <div class="size-label">2560 x 1440px</div>

  <section class="banner">
    <svg class="banner-art" viewBox="0 0 2560 425" preserveAspectRatio="none" aria-hidden="true">
      <defs>
        <linearGradient id="left-wave" x1="0" y1="0" x2="1" y2="0">
          <stop offset="0" stop-color="#f9cb16"/>
          <stop offset="0.35" stop-color="#a9c84a"/>
          <stop offset="0.6" stop-color="#3fb7c9"/>
          <stop offset="1" stop-color="#0a8fd0"/>
        </linearGradient>
        <linearGradient id="right-wave" x1="0" y1="1" x2="1" y2="0">
          <stop offset="0" stop-color="#0a8fd0"/>
          <stop offset="0.45" stop-color="#5c9fa0"/>
          <stop offset="1" stop-color="#f4c928"/>
        </linearGradient>
        <linearGradient id="sweep" x1="0" y1="0" x2="1" y2="0">
          <stop offset="0" stop-color="#f4c21c"/>
          <stop offset="0.3" stop-color="#f9cb16"/>
          <stop offset="0.5" stop-color="#9cc454"/>
          <stop offset="0.7" stop-color="#19b3cf"/>
          <stop offset="1" stop-color="#00aeef"/>
        </linearGradient>
        <linearGradient id="top-ribbon" x1="0" y1="0" x2="1" y2="0">
          <stop offset="0" stop-color="#f9cb16"/>
          <stop offset="0.7" stop-color="#e9c72a"/>
          <stop offset="1" stop-color="#4f9fb0"/>
        </linearGradient>
      </defs>

      <path d="M0 0 H260 C240 90 270 190 330 235 C420 290 600 245 648 360 L0 360 Z" fill="url(#left-wave)"/>
      <path d="M0 130 C120 70 200 30 280 0 H400 C260 60 120 130 0 190 Z" fill="url(#top-ribbon)"/>

      <path d="M1860 360 C1900 300 1990 275 2110 262 C2230 248 2260 190 2275 120 C2295 40 2330 10 2350 0 H2560 V240 Z" fill="url(#right-wave)"/>

      <path d="M0 230 C500 350 900 390 1300 392 C1800 392 2200 320 2560 238 V425 H0 Z" fill="url(#sweep)"/>
      <path d="M0 262 C500 375 900 410 1300 412 C1800 412 2200 345 2560 262 V425 H0 Z" fill="#00aeef"/>

      <g class="hazard-stripes">
        <path d="M0 270 L460 425 H0 Z" fill="var(--deep-blue)"/>
        <path d="M0 270 L20 276 L60 350 L35 342 Z" fill="#ffffff"/>
        <path d="M78 295 L120 308 L160 375 L118 362 Z" fill="#ffffff"/>
        <path d="M160 320 L205 333 L245 395 L200 382 Z" fill="#ffffff"/>
        <path d="M245 345 L275 355 L280 405 L265 402 Z" fill="#ffffff"/>
        <path d="M0 360 L30 340 L360 425 H0 Z" fill="#00aeef"/>
      </g>
    </svg>

    <div class="recycle-mark" role="img" aria-label="Faint recycling symbol"></div>

    <div class="brand-lockup">
      <span class="brand-dot"></span>
      <h1 class="brand-name">BRULO INC.</h1>
    </div>

    <p class="service-line">ROLL-OFF DUMPSTERS</p>

    <div class="web-pill">WWW.BRULODUMPSTERS.COM</div>
  </section>
</body>
</html>
```